Tranquil Pathway Business Card

Logo attached. (will be printing onto thick white/off white textured card)

Double sided business card for two Therapists working at Tranquil Pathway.

Require one design, but with different name and mobile numbers on each card.

Target Market(s)

Medical, Health

Industry/Entity Type

Business

Contact Information for Business Card

Need one business card design, but a separate card for each person - Colin Marchetti and Marieke de Boeckx.

FRONT OF CARD

Logo

Name (Colin Marchetti on one card, Marieke de Boeckx on the other)
Professional Clinical Hypnotherapist

Consulting Rooms (Near Lindqvist Hospital)
482 Brackenfield Road
Dunmore VIC 3987

Colin@TranquilPathway.example.au OR Marieke@TranquilPathway.example.au

Mobile: 0455 872 604 (for Colin) OR
Mobile: 0467 290 518 (for Marieke)

BACK OF CARD

Logo

Website: www.TranquilPathway.example.au

Phone: 1300 958 471

Requirements
Must have
• Text and logo only. No additiional graphics.

```html
<!DOCTYPE html>
<html lang="en">
<head>
<meta charset="utf-8">
<title>Tranquil Pathway Business Card</title>
<link href="https://fonts.googleapis.com/css2?family=Open+Sans:wght@400;600;700&display=swap" rel="stylesheet">
<style>
  :root {
    --page-bg: #e9e7e3;
    --card-dark: #2a292b;
    --card-light: #ffffff;
    --navy: #23306b;
    --grey: #6a6a6c;
    --grey-light: #8e8e90;
    --rule-dark: #7a7a7c;
    --white: #ffffff;
  }
  * { margin: 0; padding: 0; box-sizing: border-box; }
  html, body { width: 1200px; height: 1200px; overflow: hidden; }
  body {
    background: var(--page-bg);
    font-family: "Open Sans", Arial, sans-serif;
    position: relative;
  }
  .card {
    position: absolute;
    left: 150px;
    width: 900px;
    height: 514px;
    box-shadow: 0 6px 18px rgba(0,0,0,0.18);
  }
  .card--back { top: 56px; background: var(--card-dark); }
  .card--front { top: 630px; background: var(--card-light); }

  .brand { position: absolute; display: flex; align-items: center; }
  .brand__dot {
    width: 112px; height: 112px; border-radius: 50%;
    background: var(--navy);
  }
  .brand__rule { width: 2px; height: 118px; margin: 0 22px; }
  .brand__name {
    font-weight: 700; font-size: 40px; letter-spacing: 1px;
    text-transform: uppercase; line-height: 1;
  }
  .card--back .brand { left: 205px; top: 150px; }
  .card--back .brand__rule { background: var(--rule-dark); }
  .card--back .brand__name { color: var(--white); }
  .card--front .brand { right: 48px; top: 70px; }
  .card--front .brand__rule { background: var(--grey-light); }
  .card--front .brand__name { color: var(--navy); }

  .back-contact {
    position: absolute; left: 0; right: 0; bottom: 48px;
    display: flex; justify-content: center; align-items: center; gap: 10px;
    color: var(--white); font-size: 21px;
  }
  .back-contact svg { width: 24px; height: 24px; }

  .person { position: absolute; left: 0; top: 255px; padding-left: 44px; }
  .person__bar {
    position: absolute; left: 0; top: 12px;
    width: 14px; height: 60px; background: var(--navy);
  }
  .person__name { color: var(--navy); font-weight: 700; font-size: 30px; line-height: 1.2; }
  .person__title { color: var(--grey); font-size: 21px; line-height: 1.3; }
  .person__lines { margin-top: 14px; color: var(--grey); font-size: 21px; }
  .line { display: flex; align-items: center; gap: 10px; line-height: 1.45; }
  .line svg { width: 20px; height: 20px; flex: none; }
  .rooms { margin-top: 18px; color: var(--grey); font-size: 21px; line-height: 1.35; }
  .rooms strong { font-weight: 700; }
</style>
</head>
<body>

<section class="card card--back">
  <div class="brand">
    <div class="brand__dot"></div>
    <div class="brand__rule"></div>
    <div class="brand__name">Tranquil Pathway</div>
  </div>
  <div class="back-contact">
    <svg viewBox="0 0 24 24" aria-hidden="true">
      <circle cx="12" cy="12" r="12" fill="#ffffff"/>
      <path d="M8.2 6.5l2 2.3-1.1 1.5c.8 1.7 2 2.9 3.7 3.7l1.5-1.1 2.3 2-1.2 1.8c-4.2-.5-8-4.3-8.5-8.5z" fill="#2a292b"/>
    </svg>
    <span>1300 958 471 | www.TranquilPathway.example.au</span>
  </div>
</section>

<section class="card card--front">
  <div class="brand">
    <div class="brand__dot"></div>
    <div class="brand__rule"></div>
    <div class="brand__name">Tranquil Pathway</div>
  </div>
  <div class="person">
    <div class="person__bar"></div>
    <div class="person__name">Marieke de Boeckx</div>
    <div class="person__title">Professional Clinical Hypnotherapist</div>
    <div class="person__lines">
      <div class="line">
        <svg viewBox="0 0 20 20" aria-hidden="true">
          <circle cx="10" cy="10" r="10" fill="#23306b"/>
          <rect x="6.5" y="4.5" width="7" height="11" rx="1.2" fill="none" stroke="#fff" stroke-width="1.4"/>
        </svg>
        <span>0467 290 518</span>
      </div>
      <div class="line">
        <svg viewBox="0 0 20 20" aria-hidden="true">
          <circle cx="10" cy="10" r="10" fill="#23306b"/>
          <rect x="5" y="6.5" width="10" height="7" fill="none" stroke="#fff" stroke-width="1.3"/>
          <path d="M5 6.5l5 4 5-4" fill="none" stroke="#fff" stroke-width="1.3"/>
        </svg>
        <span>Marieke@TranquilPathway.example.au</span>
      </div>
    </div>
    <div class="rooms">
      <strong>Consulting Rooms</strong> (Near Lindqvist Hospital)<br>
      482 Brackenfield Road, Dunmore VIC 3987
    </div>
  </div>
</section>

</body>
</html>
```